Professional Business Cards

We need a nice looking, profession and modern business card for our new company. Our logo is attatched

Target Market(s)

Young Professionals

Industry/Entity Type

Financial

Contact Information for Business Card

FRONT

Morvane Tally Pty Ltd
Level 22, Halden Court, 48 Wirrapool St
Sydney NSW 2000
ABN : 57 304 918 226

Derek Wallis - Chief Operations Officer
P : 02 7153 2819
M: 0418 395 207
derek@morvanetally,com

BACK

- Cryptocurrency Exchange Services
- Cryptocurrency Mining Operations
- Cryptocurrency Investment Fund Offering

Font styles to use
Sans Serif

Colors
0255a3
9d9d9d

```html
<!DOCTYPE html>
<html lang="en">
<head>
<meta charset="utf-8">
<title>Morvane Tally – Business Card</title>
<link rel="stylesheet" href="https://fonts.googleapis.com/css2?family=Exo+2:wght@400;600;700&family=Open+Sans:wght@400;600&display=swap">
<style>
  :root {
    --brand-blue: #0255a3;
    --brand-grey: #9d9d9d;
    --text-grey: #6f6f6f;
    --card-white: #ffffff;
    --stage: #3b3b3b;
  }
  * { margin: 0; padding: 0; box-sizing: border-box; }
  html, body { width: 1200px; height: 1047px; overflow: hidden; }
  body {
    position: relative;
    background: var(--stage);
    font-family: "Open Sans", Arial, sans-serif;
  }
  .card {
    position: absolute;
    top: 374px;
    width: 522px;
    height: 299px;
    border-radius: 18px;
    overflow: hidden;
  }
  .card--front { left: 71px; background: var(--card-white); }
  .card--back { left: 606px; background: var(--brand-blue); color: var(--card-white); }

  .wordmark {
    font-family: "Exo 2", Arial, sans-serif;
    font-weight: 700;
    text-transform: uppercase;
    letter-spacing: 0.5px;
    line-height: 1;
  }
  .card--front .wordmark {
    position: absolute; left: 23px; top: 28px;
    font-size: 30px; color: var(--brand-blue);
  }
  .person { position: absolute; left: 24px; top: 121px; }
  .person__name {
    font-family: "Exo 2", Arial, sans-serif;
    font-size: 15px; font-weight: 600; letter-spacing: 0.5px;
    color: var(--brand-blue); text-transform: uppercase;
  }
  .person__title { font-size: 10.5px; color: var(--text-grey); margin-top: 1px; }

  .contacts { position: absolute; left: 24px; top: 175px; list-style: none; }
  .contacts li {
    display: flex; align-items: center; gap: 9px;
    font-size: 12px; letter-spacing: 0.4px; color: var(--text-grey);
    height: 17px;
  }
  .contacts svg { width: 9px; height: 9px; fill: var(--brand-blue); flex: none; }

  .company { position: absolute; left: 24px; top: 237px; font-size: 12px; color: var(--text-grey); line-height: 16px; }
  .company__name {
    font-family: "Exo 2", Arial, sans-serif;
    font-weight: 600; color: var(--brand-blue); text-transform: uppercase;
    letter-spacing: 0.4px;
  }
  .abn { position: absolute; left: 278px; top: 269px; font-size: 12px; color: var(--text-grey); }

  .card--back .wordmark {
    position: absolute; right: 22px; top: 140px;
    font-size: 28px; color: var(--card-white); text-align: right;
  }
  .services {
    position: absolute; right: 22px; top: 233px;
    list-style: none; text-align: right;
    font-family: "Exo 2", Arial, sans-serif;
    font-size: 12px; letter-spacing: 0.3px; line-height: 16.5px;
  }
</style>
</head>
<body>
  <section class="card card--front" aria-label="Card front">
    <div class="wordmark">Morvane Tally</div>

    <div class="person">
      <div class="person__name">Derek Wallis</div>
      <div class="person__title">Chief Operations Officer</div>
    </div>

    <ul class="contacts">
      <li>
        <svg viewBox="0 0 10 10" aria-hidden="true"><path d="M2 0.5 L3.6 0.5 L4.3 2.8 L3.2 3.7 C3.8 5 5 6.2 6.3 6.8 L7.2 5.7 L9.5 6.4 L9.5 8 C9.5 9 8.8 9.5 8 9.5 C4 9.2 0.8 6 0.5 2 C0.5 1.2 1 0.5 2 0.5 Z"/></svg>
        02 7153 2819
      </li>
      <li>
        <svg viewBox="0 0 10 10" aria-hidden="true"><path d="M2.5 0 H7.5 V10 H2.5 Z M3.4 1 V8 H6.6 V1 Z"/></svg>
        0418 395 207
      </li>
      <li>
        <svg viewBox="0 0 10 10" aria-hidden="true"><path d="M0 1.5 H10 V2.5 L5 5.5 L0 2.5 Z M0 3.6 L5 6.6 L10 3.6 V8.5 H0 Z"/></svg>
        derek@morvanetally,com
      </li>
    </ul>

    <div class="company">
      <div class="company__name">Morvane Tally Pty Ltd</div>
      <div>Level 22, Halden Court, 48</div>
      <div>Wirrapool St Sydney NSW 2000</div>
    </div>
    <div class="abn">ABN : 57 304 918 226</div>
  </section>

  <section class="card card--back" aria-label="Card back">
    <div class="wordmark">Morvane Tally</div>
    <ul class="services">
      <li>Cryptocurrency Mining Operations</li>
      <li>Cryptocurrency Exchange Services</li>
      <li>Cryptocurrency Investment Fund Offering</li>
    </ul>
  </section>
</body>
</html>
```